Window company needs new banner

Window company that has 3 focuses needs a new banner ad.

We sell window hardware
We make new sashes and windows
We restore old windows

http://www.tlsashandrenewal.com

I would like to create a new banner ad for our home page. The ad would try to capture the 3 sections listed above. I would also say they are listed in importance. Our main focus is hardware for this ad.

our best pictures are on our website.

Our suppliers websites
http://www.brindle.co.uk
http://www.kelphardware.co.uk
https://www.pellowgoods.com

Target Market(s)

Historical buildings
Restoration contractors
window restorers
DIY home owners
custom window and door fabricators- Trades people

Industry/Entity Type

Home And Garden

Font styles to use
Serif

Requirements
Must have
• Show the high level of quality of our hardware and other services

```html
<!DOCTYPE html>
<html lang="en">
<head>
<meta charset="utf-8">
<title>TL Sash &amp; Renewal — Home</title>
<link rel="stylesheet" href="https://fonts.googleapis.com/css2?family=Jost:wght@500&family=Oswald:wght@500&family=Gochi+Hand&family=Questrial&family=Cormorant+Garamond:wght@500;600&display=swap">
<style>
  :root {
    --ink: #211c1a;
    --hero: #201b19;
    --red: #e8202a;
    --stone: #c4c8c7;
    --paper: #ffffff;
    --muted: #9a9795;
    --headline: #d4d4d4;
    --black: #111111;
    --script: #555555;
  }
  * { margin: 0; padding: 0; box-sizing: border-box; }
  html, body { width: 1200px; height: 687px; overflow: hidden; background: var(--paper); }
  .page { position: relative; width: 1200px; height: 687px; overflow: hidden; background: var(--paper); }

  .site-header { position: absolute; left: 0; top: 0; width: 1200px; height: 77px; background: var(--ink); }
  .brand { position: absolute; left: 198px; top: 22px; display: flex; align-items: center; gap: 9px;
    font-family: 'Cormorant Garamond', serif; font-weight: 600; font-size: 23px; letter-spacing: 0.5px; color: var(--paper); line-height: 30px; }
  .brand-square { width: 26px; height: 26px; background: var(--red); }
  .nav-link { position: absolute; top: 31px; font-family: 'Jost', sans-serif; font-weight: 500;
    font-size: 11.5px; letter-spacing: 1.8px; color: var(--paper); white-space: nowrap; text-decoration: none; line-height: 14px; }
  .nav-link.is-current { color: var(--muted); }
  .nav-blog { position: absolute; left: 941px; top: 19px; width: 74px; height: 38px; border: 2px solid var(--paper);
    display: flex; align-items: center; justify-content: center; font-family: 'Jost', sans-serif; font-weight: 500;
    font-size: 11.5px; letter-spacing: 1.8px; color: var(--paper); text-decoration: none; }

  .specialists { position: absolute; left: 194px; top: 102px; width: 330px; height: 65px; }
  .specialists-title { position: absolute; left: 0; top: 8px; font-family: 'Oswald', sans-serif; font-weight: 500;
    font-size: 20px; line-height: 24px; color: var(--black); white-space: nowrap; letter-spacing: -0.3px; }
  .specialists-script { position: absolute; left: 0; top: 32px; font-family: 'Gochi Hand', cursive;
    font-size: 25px; line-height: 28px; letter-spacing: 3.5px; color: var(--script); white-space: nowrap; }
  .divider-bar { position: absolute; top: 0; height: 65px; background: var(--black); }
  .divider-bar.thick { left: 169px; width: 7px; }
  .divider-bar.thin { left: 183px; width: 3px; }
  .sectors { position: absolute; left: 207px; top: 16px; font-family: 'Questrial', sans-serif; font-size: 16px;
    letter-spacing: 2.2px; line-height: 20px; color: var(--black); white-space: nowrap; }

  .services { position: absolute; right: 186px; top: 104px; text-align: right; font-family: 'Questrial', sans-serif;
    font-size: 20px; line-height: 19.5px; color: var(--black); white-space: nowrap; }

  .hero { position: absolute; left: 188px; top: 198px; width: 854px; height: 404px; background: var(--hero); overflow: hidden; }
  .hero-shapes { position: absolute; left: 0; top: 0; }
  .hero-headline { position: absolute; left: 30px; top: 160px; width: 420px; padding-left: 8px; text-align: center;
    font-family: 'Cormorant Garamond', serif; font-weight: 500; font-size: 34px; letter-spacing: 8px; line-height: 38px; white-space: nowrap; }
  .hero-headline .line-light { display: block; color: var(--headline); }
  .hero-headline .line-accent { display: block; color: var(--red); font-weight: 600; }

  .feature-card { position: absolute; top: 621px; width: 272px; height: 66px; }
  .feature-card.hardware { left: 189px; background: linear-gradient(135deg, #5a3a22, #b08660 55%, #d8c4ad); }
  .feature-card.make { left: 478px; background: linear-gradient(180deg, #8fc1ec 0%, #a9cfe9 45%, #9a5a48 100%); }
  .feature-card.restore { left: 768px; background: linear-gradient(90deg, #d9d4cc, #f2f0ea 50%, #a8c58a); }
</style>
</head>
<body>
<div class="page">

  <header class="site-header">
    <div class="brand"><span class="brand-square"></span>TL SASH &amp; RENEWAL</div>
    <nav class="main-nav">
      <a class="nav-link is-current" style="left:487px" href="#">HOME</a>
      <a class="nav-link" style="left:555px" href="#">HARDWARE</a>
      <a class="nav-link" style="left:657px" href="#">WHAT WE MAKE</a>
      <a class="nav-link" style="left:789px" href="#">WHAT WE RESTORE</a>
      <a class="nav-blog" href="#">BLOG</a>
    </nav>
  </header>

  <section class="specialists">
    <div class="specialists-title">Window &amp; Hardware</div>
    <div class="specialists-script">Specialists</div>
    <span class="divider-bar thick"></span>
    <span class="divider-bar thin"></span>
    <div class="sectors">COMMERCIAL<br>RESIDENTIAL</div>
  </section>

  <div class="services">Hardware<br>New Windows &amp; Doors<br>Complete Restoration Services</div>

  <section class="hero">
    <svg class="hero-shapes" width="854" height="404" viewBox="0 0 854 404">
      <defs>
        <linearGradient id="hardwarePhoto" x1="0" y1="0" x2="1" y2="1">
          <stop offset="0" stop-color="#3a2a1c"/>
          <stop offset="0.5" stop-color="#b88a45"/>
          <stop offset="1" stop-color="#6b4a26"/>
        </linearGradient>
      </defs>
      <polygon points="0,0 78,0 0,78" fill="#e8202a"/>
      <rect x="22.5" y="24.5" width="812" height="358" fill="none" stroke="#ffffff" stroke-width="1"/>
      <polygon points="572,37 817,37 817,369 421,369" fill="url(#hardwarePhoto)" role="img" aria-label="Photo of polished brass sash window locks and lifts"/>
      <polygon points="854,327 854,404 777,404" fill="#c4c8c7"/>
    </svg>
    <h1 class="hero-headline">
      <span class="line-light">WE SUPPLY</span>
      <span class="line-accent">FINE HARDWARE</span>
    </h1>
  </section>

  <div class="feature-card hardware" role="img" aria-label="Photo of wood shavings and a turned timber piece"></div>
  <div class="feature-card make" role="img" aria-label="Photo of a brick house gable against blue sky"></div>
  <div class="feature-card restore" role="img" aria-label="Photo of a sash window being restored"></div>

</div>
</body>
</html>
```